Real Estate Investment Company Needs A Business Card Designed

I need a business card designed for my use. We are a real estate investment company based in Omaha, Nebraska that specializes in buying, rehabbing and selling single family and multifamily properties. Would love designs that incorporate our logo and colors

Industry/Entity Type

Business

Contact Information for Business Card

Marlow Pettigrew | President & CEO
4837 North 52nd Avenue, Ste 200
Omaha, NE 68214
(402) 555-7428
marlow@quillfenhomes.example
www.QuillfenHomes.example

Font styles to use
Serif

Colors
0255a3
3276b5

Requirements
Must have
• Our logo

```html
<!DOCTYPE html>
<html lang="en">
<head>
<meta charset="utf-8">
<title>Quillfen Homes – Business Card</title>
<link rel="stylesheet" href="https://fonts.googleapis.com/css2?family=Montserrat:wght@500;700&family=Questrial&display=swap">
<style>
  :root {
    --brand-blue: #0255a3;
    --brand-blue-light: #3276b5;
    --brand-blue-bright: #1e8fd6;
    --deep-blue: #023a86;
    --panel-grey: #c9cacc;
    --panel-grey-dark: #b5b7ba;
    --card-white: #ffffff;
    --page-bg: #ececec;
    --text-white: #ffffff;
  }
  * { margin: 0; padding: 0; box-sizing: border-box; }
  html, body {
    width: 1200px; height: 1200px; overflow: hidden;
    background: var(--page-bg);
  }
  .canvas {
    position: relative; width: 1200px; height: 1200px;
    display: flex; flex-direction: column; align-items: center;
    justify-content: center; gap: 80px;
  }
  .card {
    position: relative; width: 840px; height: 480px;
    background: var(--card-white);
    box-shadow: 0 6px 22px rgba(0,0,0,0.18);
    overflow: hidden;
  }
  /* Front */
  .front-wordmark {
    position: absolute; inset: 0;
    display: flex; align-items: center; justify-content: center; gap: 18px;
  }
  .wordmark-dot {
    width: 34px; height: 34px; border-radius: 50%;
    background: var(--brand-blue-light);
  }
  .wordmark-text {
    font-family: "Montserrat", sans-serif; font-weight: 700;
    color: var(--brand-blue); letter-spacing: 0.04em; white-space: nowrap;
  }
  .front-wordmark .wordmark-text { font-size: 54px; }

  /* Back */
  .back-shapes { position: absolute; inset: 0; }
  .back-logo {
    position: absolute; left: 50px; top: 150px;
    display: flex; align-items: center; gap: 12px;
  }
  .back-logo .wordmark-dot { width: 20px; height: 20px; }
  .back-logo .wordmark-text { font-size: 26px; }

  .name-block {
    position: absolute; left: 462px; top: 70px; width: 370px;
    font-family: "Questrial", sans-serif; text-transform: uppercase;
    white-space: nowrap;
  }
  .person-name { font-size: 32px; line-height: 1.1; color: var(--text-white); letter-spacing: 0.02em; }
  .person-title { font-size: 22px; line-height: 1.2; color: var(--brand-blue); margin-top: 6px; padding-left: 120px; }

  .tagline {
    position: absolute; left: 30px; top: 292px; width: 470px;
    font-family: "Montserrat", sans-serif; font-weight: 700;
    font-size: 13.5px; line-height: 1.35; color: var(--brand-blue);
  }
  .contact {
    font-family: "Montserrat", sans-serif; font-weight: 500;
    color: var(--text-white); line-height: 1.45;
    position: absolute; white-space: nowrap;
  }
  .contact-left { left: 30px; top: 362px; font-size: 16px; }
  .contact-right { left: 540px; top: 262px; font-size: 15px; }
  .contact-row { display: flex; align-items: flex-start; gap: 10px; }
  .contact-row svg { flex: none; margin-top: 3px; }
</style>
</head>
<body>
<main class="canvas">

  <section class="card card-front" aria-label="Card front">
    <div class="front-wordmark">
      <span class="wordmark-dot"></span>
      <span class="wordmark-text">QUILLFEN HOMES</span>
    </div>
  </section>

  <section class="card card-back" aria-label="Card back">
    <svg class="back-shapes" width="840" height="480" viewBox="0 0 840 480">
      <defs>
        <linearGradient id="blueField" x1="0" y1="1" x2="1" y2="0">
          <stop offset="0" stop-color="var(--deep-blue)"/>
          <stop offset="0.6" stop-color="var(--brand-blue)"/>
          <stop offset="1" stop-color="var(--brand-blue-bright)"/>
        </linearGradient>
        <linearGradient id="greyBand" x1="0" y1="0" x2="1" y2="0">
          <stop offset="0" stop-color="var(--panel-grey-dark)"/>
          <stop offset="1" stop-color="var(--panel-grey)"/>
        </linearGradient>
      </defs>
      <path class="tagline-band" d="M0 280 H530 V345 H0 Z" fill="url(#greyBand)"/>
      <path class="blue-field" d="M620 50 Q620 30 640 30 H840 V480 H0 V345 H490 Q510 345 510 325 V250 Q510 230 530 230 H620 Z" fill="url(#blueField)"/>
      <path class="name-panel" d="M460 60 H840 V160 H460 Q440 160 440 140 V80 Q440 60 460 60 Z" fill="var(--panel-grey)"/>
    </svg>

    <div class="back-logo">
      <span class="wordmark-dot"></span>
      <span class="wordmark-text">QUILLFEN HOMES</span>
    </div>

    <div class="name-block">
      <p class="person-name">Marlow Pettigrew</p>
      <p class="person-title">President &amp; CEO</p>
    </div>

    <p class="tagline">Specializes in Buying, Rehabbing, Selling single family and multifamily properties.</p>

    <div class="contact contact-left">
      <div class="contact-row">
        <svg width="16" height="16" viewBox="0 0 16 16" aria-hidden="true"><path d="M3 1 L6 1 L7 5 L5 6.5 Q6.5 9.5 9.5 11 L11 9 L15 10 L15 13 Q15 15 13 15 Q2 14 1 3 Q1 1 3 1 Z" fill="#fff"/></svg>
        <span>(402) 555-7428</span>
      </div>
      <div class="contact-row">
        <svg width="16" height="18" viewBox="0 0 16 18" aria-hidden="true"><path d="M8 1 A6 6 0 0 1 14 7 Q14 11 8 17 Q2 11 2 7 A6 6 0 0 1 8 1 Z" fill="#fff"/><circle cx="8" cy="7" r="2.2" fill="var(--brand-blue)"/></svg>
        <span>4837 North 52nd Avenue, Ste 200<br>Omaha, NE 68214</span>
      </div>
    </div>

    <div class="contact contact-right">
      <div class="contact-row">
        <svg width="16" height="16" viewBox="0 0 16 16" aria-hidden="true"><circle cx="8" cy="8" r="6.5" fill="none" stroke="#fff" stroke-width="1.4"/><ellipse cx="8" cy="8" rx="3" ry="6.5" fill="none" stroke="#fff" stroke-width="1.2"/><path d="M1.5 8 H14.5" stroke="#fff" stroke-width="1.2"/></svg>
        <span>www.QuillfenHomes.example</span>
      </div>
      <div class="contact-row">
        <svg width="16" height="14" viewBox="0 0 16 14" aria-hidden="true"><rect x="1" y="2" width="14" height="10" fill="#fff"/><path d="M1 2 L8 8 L15 2" fill="none" stroke="var(--brand-blue)" stroke-width="1.4"/></svg>
        <span>marlow@quillfenhomes.example</span>
      </div>
    </div>
  </section>

</main>
</body>
</html>
```